Website for Healthy Energy Bars

I need the layout for a website that will allow customers to purchase three different energy bars. It should have a slide show of pictures on the front page and the following tabs: About, Nutrition Info, FAQ

The website colors should not conflict with the colors of the company logo. Other than that I am open to design ideas and concepts.

Target Market(s)

Health-Conscious Eaters

Industry/Entity Type

Purchase

Number of Pages Required

3 page

Requirements
Must have
• Logo and pictures of the product
Should not have
• Colors that conflict with the logo colors

```html
<!DOCTYPE html>
<html lang="en">
<head>
<meta charset="utf-8">
<title>Leafbolt – Energy Bars</title>
<link href="https://fonts.googleapis.com/css2?family=Open+Sans:wght@400;600;700&family=Oswald:wght@400;500&display=swap" rel="stylesheet">
<style>
  :root {
    --green: #8cc63f;
    --green-dark: #6fa52a;
    --green-soft: #e9f4db;
    --ink: #4a4a4a;
    --muted: #9a9a9a;
    --line: #e2e2e2;
    --canvas: #e4e4e4;
    --white: #ffffff;
    --red: #b3202a;
  }
  * { box-sizing: border-box; margin: 0; padding: 0; }
  html, body { width: 820px; height: 1200px; overflow: hidden; }
  body {
    background: var(--canvas);
    font-family: "Open Sans", Arial, sans-serif;
    color: var(--ink);
  }
  .page {
    position: absolute; left: 30px; top: 0; width: 760px; height: 1200px;
    background: var(--white);
  }

  /* header */
  .header { position: relative; height: 100px; }
  .brand {
    position: absolute; left: 18px; top: 24px;
    display: flex; align-items: center; gap: 8px;
    font-size: 30px; font-weight: 700; color: var(--green);
  }
  .brand-dot { width: 22px; height: 22px; border-radius: 50%; background: var(--green); }
  .top-links {
    position: absolute; left: 200px; top: 8px;
    display: flex; gap: 12px; font-size: 9px; color: var(--muted);
  }
  .top-links span::before {
    content: ""; display: inline-block; width: 6px; height: 6px;
    background: var(--green); margin-right: 4px; vertical-align: middle;
  }
  .social { position: absolute; right: 18px; top: 6px; display: flex; gap: 6px; }
  .social i, .footer-social i { display: block; width: 20px; height: 20px; background: var(--green); }
  .social i.ghost { background: var(--line); }
  .phone {
    position: absolute; left: 200px; top: 58px;
    display: flex; align-items: center; gap: 6px;
    font-size: 18px; color: var(--green); font-weight: 600;
  }
  .search {
    position: absolute; left: 455px; top: 60px; width: 150px; height: 24px;
    border: 1px solid var(--line); display: flex;
  }
  .search span { flex: 1; font-size: 10px; color: var(--muted); padding: 5px 6px; }
  .search b { width: 28px; background: var(--green); }
  .select { position: absolute; top: 60px; width: 62px; height: 24px; border: 1px solid var(--line); font-size: 10px; color: var(--muted); padding: 5px 6px; }

  /* nav */
  .nav {
    position: absolute; left: 0; top: 104px; width: 760px; height: 46px;
    background: var(--green); display: flex; align-items: center; padding: 0 10px;
  }
  .nav a {
    color: var(--white); text-decoration: none; font-size: 13px; font-weight: 600;
    padding: 0 10px; line-height: 46px;
  }
  .nav a.active { background: var(--green-dark); }
  .nav .cart { margin-left: auto; }

  /* slider */
  .slider {
    position: absolute; left: 18px; top: 164px; width: 724px; height: 246px;
    background: linear-gradient(100deg, #f3f0e8 0%, #e7dfce 35%, #b22a2c 55%, #7a1016 100%);
  }
  .slide-title {
    position: absolute; right: 80px; top: 40px;
    font-family: "Oswald", Arial, sans-serif; font-size: 32px; line-height: 1;
    color: var(--green); font-weight: 500; text-transform: uppercase;
  }
  .pager { position: absolute; right: 14px; bottom: 14px; display: flex; gap: 4px; }
  .pager span {
    width: 20px; height: 20px; font-size: 11px; text-align: center; line-height: 20px;
    background: var(--white); color: var(--ink);
  }
  .pager span.on { background: var(--green); color: var(--white); }

  /* featured */
  .featured {
    position: absolute; left: 18px; top: 432px; width: 724px;
    display: flex; justify-content: space-between;
  }
  .card { width: 220px; text-align: center; }
  .card-media {
    position: relative; height: 160px;
    background: linear-gradient(180deg, #f4f4f4, #dedede);
    border: 1px solid var(--line);
  }
  .price-tag {
    position: absolute; left: 0; top: 0;
    width: 0; height: 0; border-top: 70px solid var(--green); border-right: 70px solid transparent;
  }
  .price-tag span {
    position: absolute; top: -66px; left: 4px; color: var(--white);
    font-size: 11px; font-weight: 600; white-space: nowrap;
  }
  .card h3 {
    margin-top: 14px; font-family: "Oswald", Arial, sans-serif; font-weight: 500;
    font-size: 17px; line-height: 1.1; color: var(--green); text-transform: uppercase;
  }

  /* list */
  .list { position: absolute; left: 18px; top: 692px; width: 724px; }
  .row {
    display: flex; align-items: center; height: 84px;
    border-bottom: 1px solid var(--line);
  }
  .row-media { width: 130px; height: 58px; background: linear-gradient(90deg, #f0e6d2, #c98a4a, #f0e6d2); border-radius: 4px; }
  .row-info { flex: 1; padding-left: 22px; }
  .row-info h4 { font-size: 11px; color: var(--green); font-weight: 700; text-transform: uppercase; }
  .row-info p { font-size: 7.5px; color: var(--muted); width: 300px; margin-top: 4px; line-height: 1.4; }
  .prices { margin-top: 6px; margin-left: 140px; display: flex; align-items: center; gap: 8px; }
  .now { font-size: 14px; font-weight: 600; color: var(--ink); }
  .was { font-size: 10px; color: var(--muted); text-decoration: line-through; }
  .off { font-size: 8px; background: var(--green); color: var(--white); padding: 1px 4px; }
  .buy { width: 120px; text-align: center; }
  .buy button {
    border: 0; background: var(--green); color: var(--white);
    font: 600 9px "Open Sans", Arial, sans-serif; padding: 8px 14px;
  }
  .stars { margin-top: 8px; display: flex; justify-content: center; gap: 3px; }
  .stars i { width: 8px; height: 8px; border-radius: 50%; background: var(--red); }
  .stars i.off-star { background: var(--line); }

  /* map */
  .map {
    position: absolute; left: 18px; top: 955px; width: 724px; height: 180px;
    background: linear-gradient(135deg, #e8e4d8, #d9dfcf 50%, #e6e1d4);
  }

  /* footer */
  .footer-social { position: absolute; left: 0; width: 760px; top: 1148px; display: flex; justify-content: center; gap: 8px; }
  .copyright { position: absolute; left: 0; width: 760px; top: 1178px; text-align: center; font-size: 8px; color: var(--muted); }
</style>
</head>
<body>
<div class="page">
  <header class="header">
    <div class="brand"><span class="brand-dot"></span>Leafbolt</div>
    <nav class="top-links">
      <span>Home</span><span>My Account</span><span>Shopping Cart</span>
      <span>Checkout</span><span>Create an Account</span><span>Login</span>
    </nav>
    <div class="social"><i></i><i></i><i class="ghost"></i><i class="ghost"></i></div>
    <div class="phone">
      <svg width="16" height="16" viewBox="0 0 24 24"><path fill="#8cc63f" d="M6.6 10.8a15 15 0 0 0 6.6 6.6l2.2-2.2c.3-.3.7-.4 1-.2 1.1.4 2.3.6 3.6.6.6 0 1 .4 1 1V20c0 .6-.4 1-1 1A17 17 0 0 1 3 4c0-.6.4-1 1-1h3.5c.6 0 1 .4 1 1 0 1.3.2 2.5.6 3.6.1.3 0 .7-.2 1z"/></svg>
      555-010-2040
    </div>
    <div class="search"><span>Search</span><b></b></div>
    <div class="select" style="left:612px">EN</div>
    <div class="select" style="left:680px">USD</div>
  </header>

  <nav class="nav">
    <a class="active" href="#">ONLINE STORE</a>
    <a href="#">ABOUT US</a>
    <a href="#">NUTRITION INFO</a>
    <a href="#">FAQ</a>
    <a href="#">CONTACT</a>
    <svg class="cart" width="30" height="26" viewBox="0 0 30 26"><path d="M2 3h5l4 14h13l3-10H9" fill="none" stroke="#fff" stroke-width="2.4"/><circle cx="12" cy="22" r="2.2" fill="#fff"/><circle cx="22" cy="22" r="2.2" fill="#fff"/></svg>
  </nav>

  <section class="slider" role="img" aria-label="Slideshow photo of energy bar box, cashews and fresh cherries">
    <h2 class="slide-title">Cherry Cashew<br>Crunch Bar</h2>
    <div class="pager"><span class="on">1</span><span>2</span><span>3</span></div>
  </section>

  <section class="featured">
    <article class="card">
      <div class="card-media" role="img" aria-label="Coconut cashew chew bar box"><div class="price-tag"><span>$ 60.00</span></div></div>
      <h3>Coconut Cashew<br>Chew Bar</h3>
    </article>
    <article class="card">
      <div class="card-media" role="img" aria-label="Cherry cashew crunch bar box"><div class="price-tag"><span>$ 60.00</span></div></div>
      <h3>Cherry Cashew<br>Crunch Bar</h3>
    </article>
    <article class="card">
      <div class="card-media" role="img" aria-label="Chocolate almond crunch bar box"><div class="price-tag"><span>$ 60.00</span></div></div>
      <h3>Chocolate Almond<br>Crunch Bar</h3>
    </article>
  </section>

  <section class="list">
    <div class="row">
      <div class="row-media" role="img" aria-label="Chocolate almond crunch bar"></div>
      <div class="row-info">
        <h4>Chocolate Almond Crunch Bar</h4>
        <p>Dark cocoa, roasted almonds and dates pressed into a crisp plant bar with ten grams of protein and no added sugar.</p>
        <div class="prices"><span class="now">$ 5.00</span><span class="was">$ 7.00</span><span class="off">-20%</span></div>
      </div>
      <div class="buy"><button>ADD TO CART</button><div class="stars"><i></i><i></i><i></i><i class="off-star"></i></div></div>
    </div>
    <div class="row">
      <div class="row-media" role="img" aria-label="Coconut cashew chew bar"></div>
      <div class="row-info">
        <h4>Coconut Cashew Chew Bar</h4>
        <p>Toasted coconut and whole cashews folded into a soft chewy bar, sweetened only with dates and a pinch of sea salt.</p>
        <div class="prices"><span class="now">$ 5.00</span><span class="was">$ 7.00</span><span class="off">-20%</span></div>
      </div>
      <div class="buy"><button>ADD TO CART</button><div class="stars"><i></i><i></i><i></i><i class="off-star"></i></div></div>
    </div>
    <div class="row">
      <div class="row-media" role="img" aria-label="Cherry cashew crunch bar"></div>
      <div class="row-info">
        <h4>Cherry Cashew Crunch Bar</h4>
        <p>Tart cherries and crunchy cashews bound with oats and brown rice syrup for steady energy on long days outdoors.</p>
        <div class="prices"><span class="now">$ 5.00</span><span class="was">$ 7.00</span><span class="off">-20%</span></div>
      </div>
      <div class="buy"><button>ADD TO CART</button><div class="stars"><i></i><i></i><i></i><i class="off-star"></i></div></div>
    </div>
  </section>

  <section class="map" role="img" aria-label="Street map showing the store location"></section>

  <footer>
    <div class="footer-social"><i></i><i></i><i></i><i></i></div>
    <p class="copyright">© 2014 LEAFBOLT</p>
  </footer>
</div>
</body>
</html>
```